Flyer für Trauerredner
Vielen Dank an das Designer-Team von stormbridge! Sie würden nicht müde, auch die letzten Änderungswünsche umzusetzen und dies sehr professionell. Mein Kompliment und meine Empfehlung für künftige Projekte! Gern wieder! Beste Grüße Bernd Salewski
Zielgruppe
Ich starte in Kürze als (freier, nicht-kirchlicher) Trauerredner und werde individuelle Trauerfeiern organisieren und durchführen.
Später sollen evtl. Trauerbegleitung für Angehörige und Beratung bei der Bestattung und Bestattungsvorsorge hinzukommen.
Als Zielgruppe würde ich zunächst die Bestatter in meiner Umgebung (Berlin und Umland) sehen, nach und nach auch Direktanfragen von Privatpersonen, die mich bei einer Trauerfeier gehört haben.
Aufgabenstellung
Der Flyer sollte modern und relativ schlicht gestaltet sein, ohne kirchliche Symbole.
Bei den Maßen bin ich offen, als Maximum sehe ich DIN lang/quer, sodass dieser per Brief verschickt werden kann, ansonsten zum Mitnehmen für Trauergäste auf Trauerfeiern/Bestattungen.
Ich habe 'nachklang-beispiel.example' als Webadresse reserviert. Dies soll künftig auch die Firmenbezeichnung sein. Eventuell könnte man einen QR-Code verwenden?
Später kommen noch eine Visitenkarte und eine Landing-Page hinzu, vielleicht auch noch Briefpapier.
Auf dem Flyer sollte ein passender/moderner (kann auch ein doppeldeutig-witziger) Slogan stehen.
(leider habe ich 'Jedes Leben ist der Rede wert' bei einem Kollegen gesehen, somit scheidet das aus, schade!)
Sicherlich lässt sich etwas ähnliches finden.
Weitere kurze Texte reiche ich nach, nur Aufzählungen von Dienstleistungen oder Schlagwörter, kein Fließtext.
Meine Kontaktdaten sollten auf die Rückseite des Flyers.

```html
<!DOCTYPE html>
<html lang="de">
<head>
<meta charset="utf-8">
<title>Nachklang – Flyer Innenseite</title>
<link rel="stylesheet" href="https://fonts.googleapis.com/css2?family=Gelasio:wght@700&family=Open+Sans:wght@400;700&display=swap">
<style>
  :root {
    --slate: #5e6d71;
    --paper: #f3f3f2;
    --ink: #2b2e30;
    --ink-soft: #4a4e50;
    --white: #ffffff;
    --photo-dark: #6f7274;
    --photo-light: #d9dadb;
  }
  * { box-sizing: border-box; margin: 0; padding: 0; }
  html, body { width: 1200px; height: 907px; overflow: hidden; }
  body { background: #e6e6e4; position: relative; font-family: "Open Sans", sans-serif; }

  .flyer {
    position: absolute; left: 48px; top: 63px;
    width: 1104px; height: 780px;
    background: var(--paper);
    overflow: hidden;
    box-shadow: 0 6px 24px rgba(0,0,0,.12);
  }
  .edge-band { position: absolute; top: 0; bottom: 0; width: 34px; background: var(--slate); }
  .edge-band--left { left: 0; }
  .edge-band--right { right: 0; }

  .fold { position: absolute; top: 0; bottom: 0; width: 1px; background: rgba(0,0,0,.06); }
  .fold--one { left: 368px; }
  .fold--two { left: 736px; }

  .arc { position: absolute; left: 0; top: 0; }

  .photo { position: absolute; }
  .photo--bird {
    left: 34px; top: 300px; width: 400px; height: 480px;
    background: radial-gradient(ellipse 45% 50% at 48% 40%, var(--photo-dark) 0%, #9a9c9e 40%, rgba(243,243,242,0) 75%);
  }
  .photo--berries {
    left: 960px; top: 0; width: 110px; height: 780px;
    background: linear-gradient(180deg, rgba(243,243,242,0) 0%, #b5b7b8 20%, #8c8f91 55%, #6e7274 100%);
    opacity: .8;
  }
  .photo--leaves {
    left: 760px; top: 620px; width: 200px; height: 160px;
    background: radial-gradient(ellipse 70% 80% at 100% 100%, #7c8082 0%, rgba(243,243,242,0) 80%);
  }

  .heading {
    font-family: "Gelasio", serif; font-weight: 700;
    text-transform: uppercase; letter-spacing: .08em;
    font-size: 17px; color: var(--ink);
  }
  .body-text { font-size: 15px; line-height: 1.45; color: var(--ink-soft); }

  .vision { position: absolute; left: 90px; top: 140px; width: 250px; text-align: center; }
  .vision .heading { margin-bottom: 22px; }

  .quote { position: absolute; left: 382px; top: 50px; width: 340px; text-align: center; color: var(--white); }
  .quote__text {
    font-family: "Gelasio", serif; font-weight: 700; text-transform: uppercase;
    letter-spacing: .08em; font-size: 20px; line-height: 1.3;
  }
  .quote__author { margin-top: 22px; font-size: 15px; color: #e4e8e9; }

  .sender { position: absolute; left: 368px; width: 368px; top: 678px; text-align: center; color: var(--ink); }
  .sender__name { font-weight: 700; font-size: 10px; letter-spacing: .12em; text-transform: uppercase; }
  .sender__web { margin-top: 12px; font-size: 16px; }

  .services { position: absolute; left: 760px; top: 222px; width: 230px; text-align: center; }
  .services > .heading { margin-bottom: 8px; }
  .service { margin-bottom: 38px; }
  .service__title {
    font-weight: 700; font-size: 14px; text-transform: uppercase;
    line-height: 1.3; color: var(--ink); margin-bottom: 12px;
  }
  .service__text { font-size: 14px; line-height: 1.45; color: var(--ink-soft); }
</style>
</head>
<body>
  <main class="flyer">
    <div class="photo photo--bird" role="img" aria-label="Schwarzweißfoto eines auffliegenden Vogels mit ausgebreiteten Flügeln"></div>
    <div class="photo photo--berries" role="img" aria-label="Schwarzweißfoto eines Zweigs mit Beeren am rechten Rand"></div>
    <div class="photo photo--leaves" role="img" aria-label="Schwarzweißfoto von Blättern und Beeren"></div>

    <div class="edge-band edge-band--left"></div>
    <div class="edge-band edge-band--right"></div>
    <div class="fold fold--one"></div>
    <div class="fold fold--two"></div>

    <svg class="arc" width="1104" height="780" viewBox="0 0 1104 780" aria-hidden="true">
      <circle cx="552" cy="-110" r="330" fill="var(--slate)"/>
    </svg>

    <section class="vision">
      <h2 class="heading">Unsere Vision</h2>
      <p class="body-text">We garantieren, dass wir Ihnen und Ihrer Familie die beste Erfahrung für die unvermeidliche Zukunft bieten können.</p>
    </section>

    <blockquote class="quote">
      <p class="quote__text">„Das Lied ist zu Ende, aber die Melodie klingt nach.“</p>
      <p class="quote__author">Ilse Marbach</p>
    </blockquote>

    <footer class="sender">
      <p class="sender__name">Nachklang</p>
      <p class="sender__web">www.nachklang-beispiel.example</p>
    </footer>

    <section class="services">
      <h2 class="heading">Leistungen</h2>
      <div class="service">
        <h3 class="service__title">Moderne und ansprechende Trauerzeremonien</h3>
        <p class="service__text">Persönliche Trauerreden für einen würdigen Abschied</p>
      </div>
      <div class="service">
        <h3 class="service__title">Unterstützung bei der Gestaltung der Zeremonie</h3>
        <p class="service__text">Diskrete und unterstützende Betreuung</p>
      </div>
      <div class="service">
        <h3 class="service__title">Diskretion und Verständnis in schweren Zeiten</h3>
        <p class="service__text">Gemeinsam gestalten wir einen unvergesslichen Abschied</p>
      </div>
    </section>
  </main>
</body>
</html>
```